Prestige Car Bodyshop Business Card

We are a car bodyshop based in the UK. Our customer base is mainly prestige high-value vehicles. I am looking for a classy and stylish business card design for my staff to give out to customers, with their direct email and phone number, as well as our main email and phone number with address details

I am also looking to have a general business card design with just our main company address and contact details, but also have a space to add a manufacturer approval logo (i.e Falcora, Vexa, Torvik etc... logo) in the corner somewhere.

I do not particularly want any outlines or pictures of cars on the card, I would just like a quality high-end look.

Please feel free to get in touch if you have any questions or queries?

Many Thanks

Gordon

Target Market(s)

Prestige vehicle owners

Industry/Entity Type

Automotive

Contact Information for Business Card

I am looking for a classy and stylish business card design for my staff to give out to customers, with their direct email and phone number, as well as our main email and phone number with address details

Font styles to use
Sans Serif

Colors

Designer to choose colors to be used in the design.

Requirements
Nice to have
• I do not particularly want any outlines or pictures of cars on the card, I would just like a quality high-end look.

```html
<!DOCTYPE html>
<html lang="en">
<head>
<meta charset="utf-8">
<title>Hartwell – Business Card</title>
<link rel="stylesheet" href="https://fonts.googleapis.com/css2?family=Montserrat:wght@700&family=Work+Sans:wght@400&display=swap">
<style>
  :root {
    --stage: #2c2c2d;
    --card-white: #ffffff;
    --navy: #1f3566;
    --orange: #f08a24;
    --blue-start: #1a68b0;
    --blue-end: #1e3466;
    --text-dark: #253a66;
  }
  html, body {
    margin: 0;
    padding: 0;
    width: 1200px;
    height: 930px;
    overflow: hidden;
    background: var(--stage);
  }
  .canvas {
    position: relative;
    width: 1200px;
    height: 930px;
  }
  .card {
    position: absolute;
    left: 278px;
    width: 644px;
    height: 368px;
    border-radius: 24px;
    overflow: hidden;
  }
  .card--front { top: 76px; background: var(--card-white); }
  .card--back {
    top: 486px;
    background: linear-gradient(90deg, var(--blue-start), var(--blue-end));
  }

  .brand { position: absolute; font-family: "Work Sans", sans-serif; }
  .brand__mark { position: absolute; border-radius: 50%; }
  .brand__name {
    position: absolute;
    margin: 0;
    font-weight: 400;
    white-space: nowrap;
    line-height: 1;
  }

  /* front brand */
  .card--front .brand__mark {
    left: 322px; top: 36px; width: 96px; height: 96px;
    background: var(--navy);
  }
  .card--front .brand__name {
    left: 432px; top: 67px; font-size: 34px; color: var(--navy);
  }

  /* back brand */
  .card--back .brand__mark {
    left: 138px; top: 122px; width: 124px; height: 124px; background: var(--card-white);
  }
  .card--back .brand__name {
    left: 280px; top: 162px; font-size: 44px; color: var(--card-white);
  }

  /* staff details */
  .staff { position: absolute; left: 40px; top: 170px; font-family: "Work Sans", sans-serif; }
  .staff__name {
    margin: 0;
    font-family: "Montserrat", sans-serif;
    font-weight: 700;
    font-size: 25px;
    letter-spacing: 0.8px;
    color: var(--navy);
    line-height: 1;
  }
  .staff__role { margin: 5px 0 0; font-size: 15px; color: var(--orange); line-height: 1; }
  .staff__address {
    margin: 12px 0 0;
    font-style: normal;
    font-size: 16px;
    line-height: 20px;
    color: var(--text-dark);
  }
  .contact { list-style: none; margin: 9px 0 0; padding: 0; }
  .contact__item {
    display: flex;
    align-items: center;
    height: 20.5px;
    font-size: 16px;
    color: var(--text-dark);
  }
  .contact__icon { width: 11px; height: 11px; margin: 0 12px 0 0; flex: none; }
</style>
</head>
<body>
<div class="canvas">

  <section class="card card--front" aria-label="Business card front">
    <div class="brand">
      <span class="brand__mark" aria-hidden="true"></span>
      <p class="brand__name">HARTWELL</p>
    </div>

    <div class="staff">
      <h1 class="staff__name">MARCUS BELL</h1>
      <p class="staff__role">Director</p>
      <address class="staff__address">48 Marlow Road<br>Kingsford, KB4 7TR</address>
      <ul class="contact">
        <li class="contact__item">
          <svg class="contact__icon" viewBox="0 0 12 12" aria-hidden="true">
            <path d="M2.5 1 L4.5 1 L5.2 3.4 L4 4.4 Q5 7 7.6 8 L8.6 6.8 L11 7.5 L11 9.5 Q10.5 11 9 11 Q1 10 1 2.8 Q1 1.3 2.5 1 Z" fill="none" stroke="#f08a24" stroke-width="1.1"/>
          </svg>
          512 555 0148
        </li>
        <li class="contact__item">
          <svg class="contact__icon" viewBox="0 0 12 12" aria-hidden="true">
            <rect x="0.8" y="2.3" width="10.4" height="7.4" rx="1" fill="none" stroke="#f08a24" stroke-width="1.1"/>
            <path d="M1 2.8 L6 6.5 L11 2.8" fill="none" stroke="#f08a24" stroke-width="1.1"/>
          </svg>
          info@hartwellbody.com
        </li>
        <li class="contact__item">
          <svg class="contact__icon" viewBox="0 0 12 12" aria-hidden="true">
            <g fill="none" stroke="#f08a24" stroke-width="1">
              <circle cx="6" cy="6" r="5"/>
              <ellipse cx="6" cy="6" rx="2.2" ry="5"/>
              <path d="M1 6 H11 M1.8 3.5 H10.2 M1.8 8.5 H10.2"/>
            </g>
          </svg>
          www.hartwellbody.com
        </li>
      </ul>
    </div>
  </section>

  <section class="card card--back" aria-label="Business card back">
    <div class="brand">
      <span class="brand__mark" aria-hidden="true"></span>
      <p class="brand__name">HARTWELL</p>
    </div>
  </section>

</div>
</body>
</html>
```